Business card for a doctor's practice

Would like a business card for a Pulmonary ( lung) doctor. I would like to include a logo with something in reference to air or oxygen or lungs. Would like the color red included somehow. Name of the company is Breathwell Medical Associates of Eastern Ridgeford and we specialize in Pulmonary Medicine,. I would like something streamlined and modern
Target Market(s)
Patients, hospitals, other doctors
Industry/Entity Type
Business
Contact Information for Business Card
Would like business details superimposed on a logo somehow

```html
<!DOCTYPE html>
<html lang="en">
<head>
<meta charset="UTF-8">
<title>Breathwell Medical Associates – Business Card</title>
<link href="https://fonts.googleapis.com/css2?family=Cinzel:wght@400;500&display=swap" rel="stylesheet">
<style>
  :root {
    --page: #e9e9e9;
    --card: #ffffff;
    --card-tint: #ececec;
    --brand-red: #d9141b;
    --brand-red-dark: #b80f14;
    --ink: #1d1d1d;
    --accent-green: #2f8f2a;
    --icon-teal: #1f7f95;
  }
  * { box-sizing: border-box; margin: 0; padding: 0; }
  html, body {
    width: 1200px;
    height: 1200px;
    overflow: hidden;
    background: var(--page);
  }
  body {
    display: flex;
    align-items: center;
    justify-content: center;
    font-family: "Cinzel", "Trajan Pro", serif;
  }
  .business-card {
    position: relative;
    width: 1040px;
    height: 594px;
    background: var(--card);
    overflow: hidden;
    box-shadow: 0 10px 30px rgba(0,0,0,0.18);
  }
  .card-texture {
    position: absolute;
    inset: 0;
    background:
      radial-gradient(ellipse at 85% 15%, var(--card-tint) 0%, rgba(236,236,236,0) 45%),
      radial-gradient(ellipse at 90% 85%, var(--card-tint) 0%, rgba(236,236,236,0) 40%),
      radial-gradient(ellipse at 10% 80%, var(--card-tint) 0%, rgba(236,236,236,0) 40%),
      linear-gradient(180deg, #fafafa 0%, #f2f2f2 100%);
  }
  .brand-panel {
    position: absolute;
    left: 0;
    top: 0;
    width: 478px;
    height: 548px;
    background: linear-gradient(160deg, #f7f7f7 0%, #ececec 100%);
    box-shadow: 10px 6px 18px rgba(0,0,0,0.12);
  }
  .brand-mark {
    position: absolute;
    left: 44px;
    top: 150px;
    width: 390px;
    display: flex;
    flex-direction: column;
    align-items: center;
    gap: 26px;
  }
  .brand-dot {
    width: 74px;
    height: 74px;
    border-radius: 50%;
    background: var(--brand-red);
  }
  .brand-name {
    color: var(--brand-red);
    font-weight: 500;
    font-size: 30px;
    line-height: 1.25;
    text-align: center;
    letter-spacing: 0.5px;
  }
  .contact-block {
    position: absolute;
    left: 540px;
    top: 150px;
    color: var(--ink);
  }
  .person-name {
    font-size: 40px;
    font-weight: 400;
    letter-spacing: 1px;
    line-height: 1;
  }
  .person-title {
    margin-top: 6px;
    font-size: 15px;
    color: var(--accent-green);
    letter-spacing: 1px;
  }
  .address {
    margin-top: 30px;
    font-size: 16px;
    line-height: 1.25;
    letter-spacing: 0.5px;
    padding-left: 30px;
  }
  .contact-list {
    list-style: none;
    margin-top: 6px;
    font-size: 16px;
    letter-spacing: 0.5px;
  }
  .contact-list li {
    display: flex;
    align-items: center;
    gap: 14px;
    height: 28px;
  }
  .contact-list svg { width: 18px; height: 18px; flex: none; }
  .footer-band {
    position: absolute;
    left: 0;
    right: 0;
    bottom: 0;
    height: 46px;
    background: linear-gradient(180deg, var(--brand-red) 0%, var(--brand-red-dark) 100%);
  }
</style>
</head>
<body>
  <div class="business-card">
    <div class="card-texture" role="img" aria-label="Soft light-grey background with a faint molecule pattern"></div>

    <div class="brand-panel" role="img" aria-label="Light panel with a subtle grid pattern behind the company name"></div>

    <div class="brand-mark">
      <div class="brand-dot"></div>
      <div class="brand-name">Breathwell Medical Associates<br>of Eastern Ridgeford</div>
    </div>

    <div class="contact-block">
      <h1 class="person-name">NAME SURENAME</h1>
      <p class="person-title">YOUR TITLE / POSITION</p>
      <p class="address">YOUR ADDRESS<br>ADDRESS LINE 2<br>CITY NAME</p>
      <ul class="contact-list">
        <li>
          <svg viewBox="0 0 20 20" aria-hidden="true"><path fill="var(--icon-teal)" d="M2 7c0-2 3-4 8-4s8 2 8 4v1h-4V6.5C13 6 12 5.8 10 5.8S7 6 6 6.5V8H2zM5 9h10l2 8H3z"/></svg>
          <span>TELEPHONE NO.</span>
        </li>
        <li>
          <svg viewBox="0 0 20 20" aria-hidden="true"><rect x="2" y="4" width="16" height="12" fill="var(--icon-teal)"/><path d="M2 4l8 7 8-7" fill="none" stroke="#fff" stroke-width="1.5"/></svg>
          <span>EMAIL</span>
        </li>
        <li>
          <svg viewBox="0 0 20 20" aria-hidden="true"><circle cx="10" cy="10" r="8" fill="var(--icon-teal)"/><path d="M2 10h16M10 2c-3 3-3 13 0 16M10 2c3 3 3 13 0 16" fill="none" stroke="#fff" stroke-width="1"/></svg>
          <span>WEBSITE</span>
        </li>
      </ul>
    </div>

    <div class="footer-band"></div>
  </div>
</body>
</html>
```